Antique Booth hang tag design

We have just taken a booth in an Antique Mall. We have found that our off the shelf white hang tags look really tacky. We would like to create a Business Card size tag with our Company Name VONK, Booth Number 27 with designated lines to write Price, Description, Inventory Number.We specialize in Glassware and Antique Tools, but include many fun finds in our space. We do not want to include our phone numbers or names at this time since we are a vendor in the anitque mall.

Industry/Entity Type

Business

Contact Information for Business Card

This is actually for a business card style hang tag for the booth.

Font styles to use
Decorative
Script

Requirements
Must have
• Catchy design

```html
<!DOCTYPE html>
<html lang="en">
<head>
<meta charset="utf-8">
<title>VONK Booth Hang Tag</title>
<link rel="stylesheet" href="https://fonts.googleapis.com/css2?family=Alfa+Slab+One&family=Fira+Sans+Condensed:wght@500;600&display=swap">
<style>
  :root {
    --page: #ffffff;
    --tag-dark: #56402c;
    --tag-mid: #8a7152;
    --tag-light: #b9a67b;
    --cream: #e6cf96;
    --cream-soft: rgba(230, 207, 150, 0.55);
    --ink: #454646;
    --field: #ffffff;
  }
  html, body {
    margin: 0;
    padding: 0;
    width: 1200px;
    height: 1000px;
    overflow: hidden;
    background: var(--page);
  }
  .canvas {
    position: relative;
    width: 1200px;
    height: 1000px;
  }
  .hang-tag {
    position: absolute;
    left: 405px;
    top: 168px;
    width: 390px;
    height: 664px;
    background:
      radial-gradient(ellipse 75% 60% at 70% 62%, var(--tag-light) 0%, var(--tag-mid) 55%, var(--tag-dark) 100%);
    overflow: hidden;
  }
  .hang-hole {
    position: absolute;
    left: 182px;
    top: 12px;
    width: 26px;
    height: 26px;
    border-radius: 50%;
    background: var(--page);
  }
  .tag-art {
    position: absolute;
    left: 0;
    top: 0;
    width: 390px;
    height: 340px;
  }
  .ornament-fill { fill: var(--cream-soft); }
  .brand-name {
    font-family: "Alfa Slab One", Georgia, serif;
    font-size: 74px;
    fill: var(--cream);
    letter-spacing: 4px;
  }
  .ribbon-band { fill: var(--cream); }
  .ribbon-tail { fill: #c4ab74; }
  .ribbon-shadow { fill: var(--ink); opacity: 0.85; }
  .ribbon-text {
    font-family: "Fira Sans Condensed", Arial, sans-serif;
    font-weight: 600;
    font-size: 17px;
    fill: var(--ink);
  }
  .divider-line { stroke: var(--cream); stroke-width: 1.5; }
  .booth-label {
    font-family: "Fira Sans Condensed", Arial, sans-serif;
    font-weight: 600;
    fill: var(--cream);
  }
  .booth-label .booth-number { font-size: 28px; }
  .write-field {
    position: absolute;
    left: 37px;
    width: 316px;
    height: 60px;
    background: var(--field);
    box-sizing: border-box;
    padding: 5px 12px;
    font-family: "Fira Sans Condensed", Arial, sans-serif;
    font-weight: 600;
    font-size: 19px;
    color: var(--ink);
  }
  .write-field::after {
    content: "";
    position: absolute;
    left: 0;
    top: 100%;
    width: 100%;
    height: 10px;
    background: var(--ink);
    clip-path: polygon(36% 0, 100% 0, 100% 100%);
  }
  .field-price { top: 360px; }
  .field-description { top: 453px; }
  .field-inventory { top: 546px; }
</style>
</head>
<body>
<div class="canvas">
  <div class="hang-tag">
    <div class="hang-hole"></div>
    <svg class="tag-art" viewBox="0 0 390 340" xmlns="http://www.w3.org/2000/svg">
      <rect class="ornament-fill" x="170" y="50" width="50" height="36" rx="14" role="img" aria-label="Small lotus ornament"/>
      <rect class="ornament-fill" x="25" y="62" width="130" height="50" rx="25" role="img" aria-label="Left swirling flourish"/>
      <rect class="ornament-fill" x="235" y="62" width="130" height="50" rx="25" role="img" aria-label="Right swirling flourish"/>
      <rect class="ornament-fill" x="20" y="148" width="42" height="28" rx="14" role="img" aria-label="Left scroll ornament"/>
      <rect class="ornament-fill" x="328" y="148" width="42" height="28" rx="14" role="img" aria-label="Right scroll ornament"/>

      <text class="brand-name" x="195" y="170" text-anchor="middle">VONK</text>

      <path class="ribbon-shadow" d="M56,212 Q195,172 346,216 L352,254 Q195,212 60,250 Z"/>
      <path class="ribbon-tail" d="M62,214 L40,222 L50,238 L46,258 L70,250 Z"/>
      <path class="ribbon-tail" d="M330,216 L352,224 L344,240 L350,260 L324,252 Z"/>
      <path class="ribbon-band" d="M50,200 Q195,160 345,205 L350,243 Q195,200 55,238 Z"/>
      <path id="ribbon-curve" d="M60,226 Q195,186 342,230" fill="none"/>
      <text class="ribbon-text"><textPath href="#ribbon-curve" startOffset="50%" text-anchor="middle">Glassware and Antique Tools</textPath></text>

      <rect class="ornament-fill" x="172" y="222" width="44" height="34" rx="12" role="img" aria-label="Hanging filigree ornament"/>

      <line class="divider-line" x1="105" y1="272" x2="285" y2="272"/>
      <rect class="ornament-fill" x="95" y="267" width="16" height="10" rx="4" role="img" aria-label="Divider end ornament"/>
      <rect class="ornament-fill" x="279" y="267" width="16" height="10" rx="4" role="img" aria-label="Divider end ornament"/>
      <text class="booth-label" x="195" y="314" text-anchor="middle" font-size="18">Booth Number <tspan class="booth-number">27</tspan></text>
      <line class="divider-line" x1="105" y1="327" x2="285" y2="327"/>
      <rect class="ornament-fill" x="95" y="322" width="16" height="10" rx="4" role="img" aria-label="Divider end ornament"/>
      <rect class="ornament-fill" x="279" y="322" width="16" height="10" rx="4" role="img" aria-label="Divider end ornament"/>
    </svg>

    <div class="write-field field-price">Price</div>
    <div class="write-field field-description">Description</div>
    <div class="write-field field-inventory">Inventory Number</div>
  </div>
</div>
</body>
</html>
```